Broschüre für Hausmeisterservice
Zielgruppe
Unser Hausmeisterservice bietet zuverlässige und professionelle Dienstleistungen rund um die Immobilie. Dazu gehören unter anderem die Pflege und Wartung von Gebäuden, kleinere Reparaturen, Reinigungsarbeiten, Gartenpflege sowie Winterdienst. Unser Ziel ist es, Eigentümern, Hausverwaltungen und Unternehmen einen sorgenfreien Rundum-Service zu bieten, damit ihre Immobilien stets gepflegt und funktionstüchtig sind. Unsere Zielgruppe sind somit Hausverwaltungen, Eigentümergemeinschaften, Firmen und Privatpersonen, die Wert auf eine gepflegte Immobilie legen und einen zuverlässigen Partner suchen.
Aufgabenstellung
Corporate Design und Kommunikation:
Freundlich, vertrauenswürdig und professionell wirken
Klare, verständliche Sprache verwenden
Visuelle Elemente, die Sauberkeit, Ordnung und gepflegte Immobilien ausstrahlen
Call-to-Action:
Klare Aufforderungen zur Kontaktaufnahme, Angebotserstellung oder Terminvereinbarung.

```html
<!DOCTYPE html>
<html lang="de">
<head>
<meta charset="utf-8">
<title>FALKNER HAUSDIENST – Broschüre</title>
<link href="https://fonts.googleapis.com/css2?family=Poppins:wght@400;500;600;700&display=swap" rel="stylesheet">
<style>
:root{
  --bg:#dfdfdc;
  --paper:#f3f3f1;
  --ink:#1d1d1d;
  --muted:#555;
  --red:#e2483b;
  --red-light:#ee7f72;
  --red-dark:#cf3523;
  --card:#e6e4e1;
}
*{margin:0;padding:0;box-sizing:border-box}
html,body{width:720px;height:1200px;overflow:hidden;background:var(--bg);font-family:"Poppins",sans-serif;color:var(--ink)}
.sheet{position:absolute;left:20px;width:680px;height:560px;display:flex;box-shadow:0 6px 18px rgba(0,0,0,.12)}
.sheet--outside{top:22px}
.sheet--inside{top:618px}
.panel{position:relative;width:33.333%;height:100%;background:var(--paper);overflow:hidden}
.panel + .panel{border-left:1px solid #e2e2df}

/* Testimonials */
.review{position:absolute;left:18px;right:18px;border:1.5px solid var(--red);padding:12px 12px 10px}
.review--one{top:28px}
.review--two{top:196px}
.stars{color:var(--red);font-size:17px;letter-spacing:4px;margin-bottom:6px}
.review p{font-size:10px;line-height:1.4}
.review .author{font-weight:700;font-size:11.5px;margin-top:8px}
.photo{position:absolute;left:0;right:0;bottom:0}
.photo--terrace{height:170px;background:linear-gradient(160deg,#f3f3f1 0%,#9b6a3c 30%,#5b3b22 55%,#4f6b3a 75%,#2e2a25 100%)}
.photo--house{height:170px;background:linear-gradient(170deg,#f3f3f1 0%,#c9c3b8 25%,#2f3640 50%,#8a6a4a 72%,#d9d4cb 100%)}

/* Contact */
.contact{position:absolute;left:0;right:0;top:40px;text-align:center}
.contact__icon{width:42px;height:42px;border-radius:50%;background:var(--red);margin:0 auto 8px;display:flex;align-items:center;justify-content:center}
.contact__text{font-size:12px;margin-bottom:22px}
.illustration--worker{position:absolute;left:30px;right:30px;bottom:20px;height:250px;border-radius:8px;background:linear-gradient(170deg,#f3f3f1 0%,#f2a23a 30%,#3d8a8a 55%,#e2483b 80%,#f3f3f1 100%)}

/* Cover */
.logo-tab{position:absolute;left:50%;top:-2px;width:140px;height:110px;margin-left:-70px;border:1.5px solid var(--red);border-top:none;border-radius:0 0 70px 70px;background:#fff;display:flex;flex-direction:column;align-items:center;justify-content:center;gap:6px}
.logo-tab__dot{width:26px;height:26px;border-radius:50%;background:var(--red)}
.logo-tab__name{font-size:10px;font-weight:700;color:var(--ink)}
.cover__title{position:absolute;left:16px;right:16px;top:150px;text-align:center;font-size:13px;line-height:1.35;font-weight:400}
.cover__title strong{font-weight:700}
.cover__sub{position:absolute;left:20px;right:20px;top:218px;text-align:center;font-size:8px;color:var(--muted);line-height:1.4}
.cta{position:absolute;left:28px;right:28px;top:262px;height:30px;border-radius:5px;background:var(--red-light);color:#fff;font-size:9px;display:flex;align-items:center;justify-content:center}

/* Inside */
.section-title{display:flex;align-items:center;gap:10px;font-size:19px;font-weight:600;margin:30px 0 0 20px}
.section-title::before{content:"";width:4px;height:22px;background:var(--red)}
.about__lead{font-size:9px;font-weight:700;margin:20px 20px 6px}
.about__text{font-size:7.5px;line-height:1.45;color:var(--muted);margin:0 20px}
.signature{width:90px;height:26px;margin:16px 20px 0;background:linear-gradient(90deg,#d4d3d0,#ebeae7);border-radius:3px}
.illustration--about{position:absolute;left:22px;right:22px;bottom:24px;height:250px;border-radius:8px;background:linear-gradient(170deg,#f3f3f1 0%,#f2a23a 30%,#3d8a8a 55%,#e2483b 80%,#f3f3f1 100%)}

.panel--stats{background:linear-gradient(160deg,var(--red-light) 0%,var(--red) 45%,var(--red-dark) 100%);color:#fff;padding:46px 0 0;text-align:center}
.stat{margin-bottom:30px}
.stat__value{font-size:54px;font-weight:700;line-height:1}
.stat__label{font-size:14px;font-weight:400;margin-top:4px}

.services{margin:22px 16px 0;display:flex;flex-direction:column;gap:12px}
.service{display:flex;background:var(--card);height:104px}
.service__photo{width:86px;flex:none}
.service__body{padding:8px 7px 6px;min-width:0}
.service__body h3{font-size:8.5px;font-weight:700;line-height:1.2;margin-bottom:4px;overflow-wrap:anywhere}
.service__body p{font-size:7px;line-height:1.4;color:var(--muted)}
.photo--street{background:linear-gradient(135deg,#5d7a50,#9aa6a8,#2f4058)}
.photo--repair{background:linear-gradient(135deg,#3b3a36,#6d7b4a,#2a2a28)}
.photo--stairs{background:linear-gradient(135deg,#e8e8e6,#a5a8ab,#5c6166)}
.photo--facility{background:linear-gradient(135deg,#2c2f33,#7b7d80,#c9c6c0)}
</style>
</head>
<body>

<section class="sheet sheet--outside">
  <div class="panel panel--reviews">
    <div class="review review--one">
      <div class="stars">★★★★★</div>
      <p>FALKNER HAUSDIENST hat mein Büro gründlich gereinigt. Sie waren professionell, effizient und hinterließen einen makellosen Eindruck. Sehr empfehlenswert!</p>
      <p class="author">Gerold Sander</p>
    </div>
    <div class="review review--two">
      <div class="stars">★★★★★</div>
      <p>Ich bin mit der Rasenpflege von FALKNER HAUSDIENST sehr zufrieden. Mein Garten sieht jetzt tadellos aus. Tolles Team, großartiger Service!</p>
      <p class="author">Tobias Renner</p>
    </div>
    <div class="photo photo--terrace" role="img" aria-label="Foto: moderne Terrasse mit Holzdach und Pflanzen"></div>
  </div>

  <div class="panel panel--contact">
    <div class="contact">
      <div class="contact__icon">
        <svg width="18" height="18" viewBox="0 0 24 24"><path fill="#fff" d="M6.6 10.8a15 15 0 0 0 6.6 6.6l2.2-2.2a1 1 0 0 1 1-.25 11.4 11.4 0 0 0 3.6.57 1 1 0 0 1 1 1V20a1 1 0 0 1-1 1A17 17 0 0 1 3 4a1 1 0 0 1 1-1h3.5a1 1 0 0 1 1 1c0 1.25.2 2.45.57 3.6a1 1 0 0 1-.25 1z"/></svg>
      </div>
      <p class="contact__text">+49301234567890</p>
      <div class="contact__icon">
        <svg width="18" height="18" viewBox="0 0 24 24"><path fill="#fff" d="M3 6h18v12H3z"/><path d="M3 6l9 7 9-7" fill="none" stroke="#e2483b" stroke-width="1.6"/></svg>
      </div>
      <p class="contact__text">info@falkner-hausdienst.example</p>
    </div>
    <div class="illustration--worker" role="img" aria-label="Illustration: Hausmeister mit Putzeimer und Besen"></div>
  </div>

  <div class="panel panel--cover">
    <div class="logo-tab">
      <span class="logo-tab__dot"></span>
      <span class="logo-tab__name">FALKNER HAUSDIENST</span>
    </div>
    <h1 class="cover__title">Ihr <strong>zuverlässiger Partner</strong> für <strong>alle Reinigungs- und Wartungsdienstleistungen</strong></h1>
    <p class="cover__sub">Professionelle Reinigung, Gartenpflege,<br>Reparaturarbeiten und mehr</p>
    <div class="cta">www.falkner-hausdienst.example</div>
    <div class="photo photo--house" role="img" aria-label="Foto: modernes Wohnhaus mit Holzfassade"></div>
  </div>
</section>

<section class="sheet sheet--inside">
  <div class="panel panel--about">
    <h2 class="section-title">Über Uns</h2>
    <p class="about__lead">Die Geschichte hinter FALKNER HAUSDIENST</p>
    <p class="about__text">FALKNER HAUSDIENST steht seit 6 Jahren für verlässliche Reinigung, Pflege und Wartung. Mit einem erfahrenen Team kümmern wir uns um Ihre Immobilie, damit Sie sich entspannt auf das Wesentliche konzentrieren können.</p>
    <div class="signature" role="img" aria-label="Handschriftliche Unterschrift des Inhabers"></div>
    <div class="illustration--about" role="img" aria-label="Illustration: Hausmeister mit Reinigungsutensilien"></div>
  </div>

  <div class="panel panel--stats">
    <div class="stat"><div class="stat__value">6</div><div class="stat__label">Jahre Erfahrung</div></div>
    <div class="stat"><div class="stat__value">700+</div><div class="stat__label">Zufriedene Kunden</div></div>
    <div class="stat"><div class="stat__value">08+</div><div class="stat__label">Preisgekrönt</div></div>
    <div class="stat"><div class="stat__value">98%</div><div class="stat__label">Kundenzufriedenheit</div></div>
  </div>

  <div class="panel panel--services">
    <h2 class="section-title">Leistungen</h2>
    <div class="services">
      <article class="service">
        <div class="service__photo photo--street" role="img" aria-label="Foto: Reinigung eines Gehwegs mit Hochdruckreiniger"></div>
        <div class="service__body"><h3>Straßenreinigung</h3><p>Unser Team reinigt Gehwege, Einfahrten und Höfe gründlich und sorgt für einen gepflegten ersten Eindruck.</p></div>
      </article>
      <article class="service">
        <div class="service__photo photo--repair" role="img" aria-label="Foto: Werkzeug für Reparaturen"></div>
        <div class="service__body"><h3>Grillreparatur / Haushaltssachen</h3><p>Unsere Experten reparieren Grills und Haushaltsgeräte schnell, sauber und zu fairen Preisen.</p></div>
      </article>
      <article class="service">
        <div class="service__photo photo--stairs" role="img" aria-label="Foto: helles Treppenhaus mit Geländer"></div>
        <div class="service__body"><h3>Treppenhaus- und Fensterreinigung</h3><p>Wir sorgen für saubere Treppenhäuser und streifenfreie Fenster mit Sorgfalt und Qualität.</p></div>
      </article>
      <article class="service">
        <div class="service__photo photo--facility" role="img" aria-label="Foto: Büroflur mit Glaswänden"></div>
        <div class="service__body"><h3>Facility&shy;management</h3><p>Wir übernehmen Wartung, Kontrolle und Pflege Ihrer Liegenschaft zuverlässig aus einer Hand.</p></div>
      </article>
    </div>
  </div>
</section>

</body>
</html>
```